Harbor Current LLC

I need a business card containing the following:

HarborCurrentLLC
Certified Master Electrician
Licensed and insured
"powered by excellence"

Dale Horvath. Brian Okafor
555-014-2281 555-019-6640

HarborCurrentLLC.example

red white and blue color scheme

Industry/Entity Type

Electric Company

Contact Information for Business Card

Red white and blue coloring

Colors
ec1f27
0456a4
ffffff

Requirements
Must have
• Harbor Current
• Certified master Electrician
• Liscensed and insured
• "Powered by excellence"
• Dale Horvath. 5550142281
• Brian Okafor. 5550196640

```html
<!DOCTYPE html>
<html lang="en">
<head>
<meta charset="utf-8">
<title>Harbor Current LLC — Business Card</title>
<link href="https://fonts.googleapis.com/css2?family=Quicksand:wght@500;600;700&display=swap" rel="stylesheet">
<style>
  :root {
    --page: #ffffff;
    --blue: #0456a4;
    --blue-deep: #033d75;
    --red: #ec1f27;
    --white: #ffffff;
  }
  * { margin: 0; padding: 0; box-sizing: border-box; }
  html, body {
    width: 977px; height: 1200px; overflow: hidden;
    background: var(--page);
    font-family: "Quicksand", sans-serif;
  }
  .card {
    position: absolute; left: 130px; width: 718px; height: 410px;
    background: linear-gradient(135deg, var(--blue) 0%, var(--blue-deep) 100%);
    overflow: hidden;
  }
  .card--front { top: 153px; }
  .card--back { top: 636px; }
  .card__band {
    position: absolute; left: 0; right: 0; bottom: 0; height: 24px;
    background: var(--red);
  }
  .wordmark {
    position: absolute; color: var(--white); font-weight: 600; line-height: 1.05;
  }
  .wordmark__line { display: block; }
  .card--front .wordmark { left: 76px; top: 58px; font-size: 40px; }
  .card--back .wordmark { left: 0; right: 0; top: 120px; text-align: center; font-size: 62px; }
  .names {
    position: absolute; left: 75px; top: 207px;
    color: var(--white); font-size: 25px; font-weight: 700; line-height: 31px;
    letter-spacing: 0.5px;
  }
  .contact { position: absolute; left: 386px; top: 0; width: 320px; }
  .contact__row {
    position: absolute; left: 0; display: flex; align-items: flex-start;
  }
  .contact__row--address { top: 243px; }
  .contact__row--phone { top: 305px; }
  .contact__row--web { top: 353px; }
  .contact__icon { width: 22px; height: 22px; margin-right: 16px; margin-top: 0; fill: var(--red); flex: none; }
  .contact__text {
    color: var(--white); font-size: 16px; font-weight: 500;
    letter-spacing: 2px; line-height: 20px;
  }
  .credentials {
    position: absolute; left: 0; right: 0; top: 305px; text-align: center;
    color: var(--white); font-size: 14px; font-weight: 600;
    letter-spacing: 4px; line-height: 17.5px;
  }
</style>
</head>
<body>
  <section class="card card--front">
    <div class="wordmark">
      <span class="wordmark__line">Harbor</span>
      <span class="wordmark__line">Current LLC</span>
    </div>
    <div class="names">
      <p>Dale Horvath</p>
      <p>Brian Okafor</p>
    </div>
    <div class="contact">
      <div class="contact__row contact__row--address">
        <svg class="contact__icon" viewBox="0 0 24 24" aria-hidden="true"><path d="M12 2a7 7 0 0 0-7 7c0 5 7 13 7 13s7-8 7-13a7 7 0 0 0-7-7zm0 9.5A2.5 2.5 0 1 1 12 6.5a2.5 2.5 0 0 1 0 5z"/></svg>
        <p class="contact__text">218 N Foundry Road<br>Millbrook, WY 82999</p>
      </div>
      <div class="contact__row contact__row--phone">
        <svg class="contact__icon" viewBox="0 0 24 24" aria-hidden="true"><path d="M6.6 10.8a15 15 0 0 0 6.6 6.6l2.2-2.2a1 1 0 0 1 1-.25 11.4 11.4 0 0 0 3.6.57 1 1 0 0 1 1 1V20a1 1 0 0 1-1 1A17 17 0 0 1 3 4a1 1 0 0 1 1-1h3.5a1 1 0 0 1 1 1c0 1.25.2 2.45.57 3.57a1 1 0 0 1-.25 1z"/></svg>
        <p class="contact__text">555-014-2281<br>555-019-6640</p>
      </div>
      <div class="contact__row contact__row--web">
        <svg class="contact__icon" viewBox="0 0 24 24" aria-hidden="true"><path d="M12 2a10 10 0 1 0 0 20 10 10 0 0 0 0-20zm6.9 6h-3a15 15 0 0 0-1.3-3.9A8 8 0 0 1 18.9 8zM12 4c.8 1.2 1.5 2.5 1.9 4h-3.8c.4-1.5 1.1-2.8 1.9-4zM4.3 14a8 8 0 0 1 0-4h3.3a16 16 0 0 0 0 4zm.8 2h3a15 15 0 0 0 1.3 3.9A8 8 0 0 1 5.1 16zm3-8h-3a8 8 0 0 1 4.3-3.9A15 15 0 0 0 8.1 8zM12 20c-.8-1.2-1.5-2.5-1.9-4h3.8c-.4 1.5-1.1 2.8-1.9 4zm2.3-6H9.7a14 14 0 0 1 0-4h4.6a14 14 0 0 1 0 4zm.3 5.9a15 15 0 0 0 1.3-3.9h3a8 8 0 0 1-4.3 3.9zm1.8-5.9a16 16 0 0 0 0-4h3.3a8 8 0 0 1 0 4z"/></svg>
        <p class="contact__text">HarborCurrentLLC.example</p>
      </div>
    </div>
    <div class="card__band"></div>
  </section>

  <section class="card card--back">
    <div class="wordmark">
      <span class="wordmark__line">Harbor</span>
      <span class="wordmark__line">Current LLC</span>
    </div>
    <div class="credentials">
      <p>HarborCurrent</p>
      <p>Certified Master Electrician</p>
      <p>Licensed and insured</p>
      <p>"powered by excellence"</p>
    </div>
    <div class="card__band"></div>
  </section>
</body>
</html>
```